LABEL for Extra Virgin Olive oil

Hi everyone!
I would please like your help with the below project.

We will start importing olive oil from Greece and I would like to create the label for the bottle.
Our goal is to create a label that will really promote the raw quality of the natural product (olive oil).
The olive oil we will import will be very high quality, but we don't want the label to promote a luxury product but more just an exceptional quality natural product that is for the many and comes directly from the producer. Potentially the label can also include images (ex. oils, olive trees, land, sea, sun) but we can evaluate that along the way.
The approximate size of the label will be 60x110 mm
The colors should be earth colors
We can discuss any potential questions as soon as we are in contact.

Thank you all in advance for your time and consideration.

Kind regards, Tobias

```html
<!DOCTYPE html>
<html lang="en">
<head>
<meta charset="UTF-8">
<title>Kalyra Extra Virgin Olive Oil – Label</title>
<link rel="stylesheet" href="https://fonts.googleapis.com/css2?family=Barlow:ital,wght@0,400;0,500;0,600;1,400&display=swap">
<style>
  :root {
    --backdrop: #efe9e1;
    --label-green: #8a9a52;
    --label-green-deep: #74853f;
    --cream: #f3ecd0;
    --title-yellow: #f5eaa5;
    --rule: rgba(243, 236, 208, 0.75);
  }
  html, body {
    margin: 0;
    padding: 0;
    width: 1200px;
    height: 800px;
    overflow: hidden;
    background: var(--backdrop);
  }
  .canvas {
    position: relative;
    width: 1200px;
    height: 800px;
  }
  .label {
    position: absolute;
    left: 404px;
    top: 40px;
    width: 392px;
    height: 720px;
    background: var(--label-green);
    color: var(--cream);
    overflow: hidden;
    box-shadow: 0 6px 24px rgba(60, 55, 40, 0.12);
  }
  .botanical {
    position: absolute;
    background: linear-gradient(135deg, var(--label-green-deep), var(--label-green));
    opacity: 0.85;
  }
  .botanical--top-right { right: 0; top: 0; width: 130px; height: 90px; border-bottom-left-radius: 70px; }
  .botanical--left { left: 0; top: 190px; width: 44px; height: 260px; border-top-right-radius: 30px; border-bottom-right-radius: 30px; }
  .botanical--bottom-left { left: 0; bottom: 0; width: 170px; height: 70px; border-top-right-radius: 60px; }
  .botanical--bottom-right { right: 0; bottom: 0; width: 90px; height: 50px; border-top-left-radius: 45px; }

  .content {
    position: absolute;
    inset: 0;
    display: flex;
    flex-direction: column;
    align-items: center;
    text-align: center;
    font-family: "Barlow", sans-serif;
  }
  .tagline {
    margin-top: 50px;
    font-weight: 500;
    font-size: 12px;
    letter-spacing: 0.3em;
  }
  .rule {
    width: 70px;
    height: 0;
    border-top: 1px solid var(--rule);
  }
  .rule--top { margin-top: 14px; }
  .brand-name {
    margin-top: 112px;
    font-weight: 500;
    font-size: 34px;
    line-height: 1;
    color: var(--cream);
  }
  .product-type {
    margin-top: 88px;
    font-weight: 500;
    font-size: 19px;
    line-height: 1;
  }
  .product-name {
    margin: 8px 0 0;
    font-weight: 600;
    font-size: 66px;
    line-height: 0.95;
    color: var(--title-yellow);
  }
  .rule--middle { margin-top: 56px; }
  .description {
    margin: 22px 0 0;
    width: 250px;
    font-style: italic;
    font-weight: 400;
    font-size: 13px;
    line-height: 1.45;
  }
  .rule--bottom { margin-top: 22px; }
</style>
</head>
<body>
  <div class="canvas">
    <div class="label">
      <div class="botanical botanical--top-right" role="img" aria-label="Engraved olive branch illustration"></div>
      <div class="botanical botanical--left" role="img" aria-label="Engraved olive leaves illustration"></div>
      <div class="botanical botanical--bottom-left" role="img" aria-label="Engraved olive branch with fruit illustration"></div>
      <div class="botanical botanical--bottom-right" role="img" aria-label="Engraved olive leaves illustration"></div>

      <div class="content">
        <div class="tagline">ORGANIC</div>
        <div class="rule rule--top"></div>
        <div class="brand-name">Kalyra</div>
        <div class="product-type">Extra Virgin</div>
        <h1 class="product-name">Olive<br>Oil</h1>
        <div class="rule rule--middle"></div>
        <p class="description">Cold pressed from hand picked olives grown on small family groves, bottled close to the harvest and sent straight from the producer to your table.</p>
        <div class="rule rule--bottom"></div>
      </div>
    </div>
  </div>
</body>
</html>
```